Creation of an elegant and modern turnkey Shopify website

Hello,

We are a new company specializing in the sale of above-ground pools. We want to create a turnkey website, ideally using Shopify. For now, we need a "showcase" site, not an e-commerce platform, with four tabs:

Home Page (an overall presentation of the company)
Our Products (an overview of all the above-ground pools we sell)
Our Projects (a page inspired by Instagram to showcase photos of our future projects)
Contact (a page with all our contact information and a contact form)

We are looking to create a highly visual, elegant, and modern website with vibrant splashes of color. We will provide the text, photos (along with instructions on where to place them on each page), and all other necessary information as attachments.

Thank you in advance for your proposals!

The Larkmere Basin Team

Target Market(s)

Targeted at Swiss customers (a translator will need to be installed for different languages)

Industry/Entity Type

Sale of customised above-ground pools

Coding

Coded - Design and coding required

Font styles to use
Sans Serif

Colors
0094D4
00A9DD
6FCCEA
C7EBF8
E9F6FB
00AB8E
00BBA5
67D7C9
C6EFE9
E9F9F6

Requirements
Must have
• A stunning, elegant and modern look
Nice to have
• Inspiration from the colors of our logo throughout the site, but in an elegant way
Should not have
• An overly classic look for swimming pool sites

```html
<!DOCTYPE html>
<html lang="en">
<head>
<meta charset="utf-8">
<title>Larkmere Basin — Above-Ground Pools</title>
<link href="https://fonts.googleapis.com/css2?family=Cormorant+Garamond:wght@500;600&family=Montserrat:wght@400;500;600;700&display=swap" rel="stylesheet">
<style>
:root{
  --blue:#0094D4;
  --blue-2:#00A9DD;
  --sky:#6FCCEA;
  --ice:#C7EBF8;
  --mist:#E9F6FB;
  --ink:#111;
  --text:#333;
  --muted:#555;
  --white:#fff;
}
*{box-sizing:border-box;margin:0;padding:0}
html,body{width:1200px;height:4146px;overflow:hidden}
body{font-family:"Montserrat",sans-serif;color:var(--text);background:var(--white);position:relative}
.display{font-family:"Cormorant Garamond",serif;font-weight:600;text-transform:uppercase;color:var(--ink);letter-spacing:.5px}
.btn{display:inline-block;background:var(--blue);color:var(--white);font-weight:700;font-size:16px;border-radius:5px;width:166px;height:47px;line-height:47px;text-align:center;text-decoration:none}
section,header,footer,div.band{position:absolute;left:0;width:1200px}

.topbar{top:0;height:45px;background:var(--blue);color:var(--white);font-size:14px;text-align:center;line-height:42px}
.nav{top:45px;height:87px;background:var(--white)}
.nav ul{list-style:none;position:absolute;left:111px;top:38px;display:flex;gap:48px;font-size:14px;color:var(--ink);font-weight:500}
.brand{position:absolute;left:536px;top:4px;width:116px;height:80px;background:var(--white);box-shadow:0 2px 8px rgba(0,0,0,.12);display:flex;align-items:center;justify-content:center;font-size:15px;font-weight:600;color:var(--blue);text-align:center;line-height:1.2}
.nav .tools{position:absolute;left:873px;top:36px;display:flex;align-items:center;gap:18px;font-size:14px;font-weight:500;color:var(--ink)}
.nav .tools svg{width:20px;height:20px;stroke:#444;fill:none;stroke-width:1.6}

.hero{top:132px;height:557px;background:linear-gradient(180deg,#6b7d3c 0%,#7a9d6c 30%,#9ccab6 60%,#6aa58e 100%);text-align:center;color:var(--white)}
.hero h1{font-family:"Cormorant Garamond",serif;font-weight:600;text-transform:uppercase;font-size:46px;line-height:60px;margin-top:154px;text-shadow:0 1px 4px rgba(0,0,0,.3)}
.hero .btn-outline{display:inline-block;margin-top:30px;border:2px solid var(--white);border-radius:6px;width:166px;height:46px;line-height:42px;font-weight:700;font-size:16px;color:var(--white)}
.dots{position:absolute;left:542px;top:456px;display:flex;gap:14px;align-items:center}
.dots span{width:11px;height:11px;border-radius:50%;background:rgba(255,255,255,.8)}
.dots span.on{width:22px;height:22px;border:3px solid var(--white);background:var(--sky)}

.intro{top:689px;height:518px;text-align:center}
.intro h2{font-size:44px;line-height:60px;margin-top:82px}
.intro p{width:800px;margin:30px auto 0;font-size:15px;line-height:34.5px}
.intro .btn{margin-top:30px}

.photo{position:absolute}
.split{height:502px}
.split .copy{position:absolute}
.split h2{font-size:44px;line-height:56px}
.split p{font-size:15px;line-height:34.5px;margin-top:18px}
.split .btn{margin-top:30px}

.personal{top:1207px}
.personal .photo{left:0;top:0;width:576px;height:502px;background:linear-gradient(160deg,#e3a64a 0%,#8c9a4a 40%,#8ec9a8 75%,#b9e1c9 100%)}
.personal .copy{left:614px;top:100px;width:430px}

.satisfaction{top:1719px;background:linear-gradient(90deg,#fff 55%,var(--mist) 100%)}
.satisfaction .photo{left:623px;top:0;width:577px;height:504px;background:linear-gradient(180deg,#e8eef2 0%,#c9dfe6 35%,#3ab0cc 60%,#6d5a3e 80%,#4f4232 100%)}
.satisfaction .copy{left:109px;top:100px;width:470px}

.contact-cta{top:2223px;height:504px;background:linear-gradient(120deg,#8fd8df 0%,#9fe0e6 55%,#a9e2ec 100%)}
.contact-cta .copy{position:absolute;left:601px;top:80px;width:440px}
.contact-cta h2{font-size:44px;line-height:56px}
.contact-cta p{font-size:15px;line-height:34.5px;margin-top:14px;color:#333}
.contact-cta .btn{margin-top:30px}
.swimmer{position:absolute;left:55px;top:140px;width:330px;height:220px;border-radius:50%;background:radial-gradient(ellipse,rgba(255,255,255,.55),rgba(255,255,255,0) 70%)}

.why{top:2727px;height:669px;text-align:center;background:linear-gradient(180deg,var(--white) 0%,var(--white) 90%,var(--mist) 100%)}
.why h2{font-size:44px;margin-top:70px;line-height:56px}
.features{position:absolute;left:112px;top:172px;display:flex;width:980px}
.feature{width:245px;text-align:center}
.feature svg{width:66px;height:74px}
.feature h3{font-size:18px;font-weight:600;color:var(--ink);line-height:30px;margin-top:16px}
.feature p{font-size:14px;line-height:29px;color:var(--muted);margin-top:22px;padding:0 10px}
.why .btn{position:absolute;left:511px;top:530px}

.dreams{top:3396px;height:306px;background:var(--mist);text-align:center}
.dreams h2{font-size:44px;margin-top:80px;line-height:56px}
.dreams .btn{margin-top:26px}

.footer{top:3702px;height:364px}
.col{position:absolute;top:90px}
.col h4{font-size:20px;font-weight:500;color:var(--ink)}
.col ul{list-style:none;margin-top:24px;font-size:14px;line-height:30px;color:#333}
.col .tag{font-size:11px;line-height:26px;margin-top:18px;width:230px}
.col .line{display:flex;gap:8px;align-items:center;font-size:14px;line-height:36px}
.col .line svg{width:14px;height:14px;fill:var(--ink)}
.col .indent{padding-left:24px;font-size:14px;line-height:36px}

.bottombar{top:4066px;height:80px;background:var(--blue);color:var(--white)}
.bottombar .copy{position:absolute;left:113px;top:30px;font-size:13px}
.social{position:absolute;left:850px;top:26px;display:flex;gap:40px}
.social span{width:28px;height:28px;border-radius:50%;border:2px solid var(--white)}
</style>
</head>
<body>

<div class="band topbar">Lorem Ipsum is simply dummy text of the printing and typesetting industry</div>

<header class="nav">
  <ul><li>HOME</li><li>ABOUT</li><li>SERVICES</li><li>CONTACT</li></ul>
  <div class="brand">Larkmere<br>Basin</div>
  <div class="tools">
    <span>ENG</span>
    <svg viewBox="0 0 20 20"><path d="M4 7l6 6 6-6"/></svg>
    <svg viewBox="0 0 20 20"><circle cx="8.5" cy="8.5" r="6"/><path d="M13 13l5 5"/></svg>
    <svg viewBox="0 0 20 20"><circle cx="10" cy="6" r="4"/><path d="M3 18c0-4 3-6 7-6s7 2 7 6z"/></svg>
    <svg viewBox="0 0 20 20"><path d="M10 17L3 10a4 4 0 016-5l1 1 1-1a4 4 0 016 5z"/></svg>
    <svg viewBox="0 0 20 20"><rect x="4" y="6" width="12" height="12"/><path d="M7 6V4h6v2"/></svg>
  </div>
</header>

<section class="hero" role="img" aria-label="Photo of a woman relaxing in a sunlit above-ground garden pool">
  <h1>Transform your garden with our<br>premium above-ground pools!</h1>
  <span class="btn-outline">Get Started</span>
  <div class="dots"><span class="on"></span><span></span><span></span><span></span></div>
</section>

<section class="intro">
  <h2 class="display">Achieve your dreams with our custom,<br>tailor-made above-ground pools</h2>
  <p>Imagine an exceptional relaxation and leisure space right in your own backyard. With our unparalleled expertise and commitment to excellence, we create above-ground pools that exceed all expectations. Our exclusive, custom-designed models are crafted to combine style, durability, and innovation, offering a unique and refined experience.</p>
  <a class="btn">Get Started</a>
</section>

<section class="split personal">
  <div class="photo" role="img" aria-label="Photo of a woman stretching in a garden pool at sunset"></div>
  <div class="copy">
    <h2 class="display">Personalized services</h2>
    <p>We understand that every garden and client is unique. That's why we offer personalized services, from design to installation and after-sales support. Our team of experts is here to answer all your questions and guide you throughout your project.</p>
    <a class="btn">Read More</a>
  </div>
</section>

<section class="split satisfaction">
  <div class="copy">
    <h2 class="display">Guaranteed satisfaction</h2>
    <p>Your satisfaction is our top priority. We are committed to providing you with exceptional service and the highest quality products. Join our community of satisfied customers who are already enjoying their custom above-ground pools. <strong style="font-size:17px;color:#222">10-Year Warranty!</strong></p>
    <a class="btn">Read More</a>
  </div>
  <div class="photo" role="img" aria-label="Photo of an above-ground pool with wood-effect siding beside a house"></div>
</section>

<section class="contact-cta" role="img" aria-label="Aerial photo of a swimmer floating in turquoise water">
  <div class="swimmer"></div>
  <div class="copy">
    <h2 class="display">Contact us today</h2>
    <p>Don't wait any longer to transform your garden into a wellness oasis. Contact us today to discover our range of customizable above-ground pools and get a tailored quote. Dive into a world of infinite possibilities with <strong style="font-size:17px;color:#222">Larkmere Basin</strong></p>
    <a class="btn">Read More</a>
  </div>
</section>

<section class="why">
  <h2 class="display">Why choose our above-ground pools?</h2>
  <div class="features">
    <div class="feature">
      <svg viewBox="0 0 66 74"><circle cx="33" cy="38" r="22" fill="none" stroke="#0094D4" stroke-width="5"/><path d="M22 38l8 8 15-16" fill="none" stroke="#0094D4" stroke-width="5"/><circle cx="33" cy="6" r="4" fill="#0094D4"/><circle cx="10" cy="14" r="3" fill="#0094D4"/><circle cx="56" cy="14" r="3" fill="#0094D4"/><path d="M26 60l7 12 7-12" fill="#0094D4"/></svg>
      <h3>Superior Quality</h3>
      <p>Each pool is constructed with high-quality materials, ensuring exceptional durability and strength.</p>
    </div>
    <div class="feature">
      <svg viewBox="0 0 66 74"><path d="M6 14h54" stroke="#0094D4" stroke-width="3"/><circle cx="6" cy="14" r="4" fill="#0094D4"/><circle cx="60" cy="14" r="4" fill="#0094D4"/><path d="M33 10l16 30-8 18H25l-8-18z" fill="#0094D4"/><circle cx="33" cy="38" r="4" fill="#fff"/><rect x="24" y="60" width="18" height="10" fill="#0094D4"/></svg>
      <h3>Elegant Design</h3>
      <p>Our pools come in a variety of styles and finishes, seamlessly blending into any garden setting.</p>
    </div>
    <div class="feature">
      <svg viewBox="0 0 66 74"><circle cx="33" cy="38" r="22" fill="none" stroke="#0094D4" stroke-width="10" stroke-dasharray="8 5"/><circle cx="33" cy="38" r="14" fill="#0094D4"/><rect x="30" y="28" width="6" height="24" fill="#fff"/></svg>
      <h3>Custom and<br>Tailor-Made</h3>
      <p>Create the pool of your dreams with our customization options, tailored to your specific tastes and needs.</p>
    </div>
    <div class="feature">
      <svg viewBox="0 0 66 74"><circle cx="28" cy="32" r="20" fill="none" stroke="#0094D4" stroke-width="10" stroke-dasharray="8 5"/><circle cx="28" cy="32" r="8" fill="#fff" stroke="#0094D4" stroke-width="4"/><circle cx="50" cy="56" r="13" fill="#0094D4"/><path d="M44 56l5 5 8-9" fill="none" stroke="#fff" stroke-width="3"/></svg>
      <h3>Easy Installation</h3>
      <p>Enjoy your new oasis quickly with our simple and fast installation process.</p>
    </div>
  </div>
  <a class="btn">Read More</a>
</section>

<section class="dreams">
  <h2 class="display">We bring your pool dreams to life!</h2>
  <a class="btn">Contact Us</a>
</section>

<footer class="footer">
  <div class="col" style="left:109px">
    <h4>Contact Us</h4>
    <p class="tag">Achieve your dreams with our custom, tailor-made above-ground pools.</p>
    <div class="line"><svg viewBox="0 0 14 14"><path d="M3 1l3 3-2 2c1 2 2 3 4 4l2-2 3 3-2 2C6 13 1 8 1 3z"/></svg>079 000 12 34</div>
    <div class="line"><svg viewBox="0 0 14 14"><path d="M7 0a5 5 0 015 5c0 4-5 9-5 9S2 9 2 5a5 5 0 015-5zm0 3a2 2 0 100 4 2 2 0 000-4z"/></svg>Elena Varsini</div>
    <div class="indent">Chemin des Tilleuls 28</div>
    <div class="indent">1800 Vevette</div>
  </div>
  <div class="col" style="left:366px">
    <h4>Quick Links</h4>
    <ul><li>Home</li><li>About</li><li>Services</li><li>Contact</li></ul>
  </div>
  <div class="col" style="left:608px">
    <h4>Other Links</h4>
    <ul><li>Privacy policy</li><li>Terms and Conditons</li></ul>
  </div>
  <div class="col" style="left:851px">
    <h4>Opening Hours</h4>
    <ul><li>Mon - Fri: 8AM - 10PM</li><li>Sat: 9AM-8PM</li><li>Sun: Closed</li></ul>
  </div>
</footer>

<div class="band bottombar">
  <span class="copy">Copyright © 2024 Larkmere Basin | All Rights Reserved</span>
  <div class="social" aria-label="Social links"><span></span><span></span><span></span><span></span></div>
</div>

</body>
</html>
```